Business Card Design Project

Hi,
This is a simple contest. The logo for the back of the card is deigned. See attached files. The front of the card must have :

Directors Name: Tobias
Mob:
e-mail:
Postal Address:
Web Page Adress:

It may also add words: "Leaders in Construction Project Management Services"

Target Market(s)

Business & Home owners alike

Industry/Entity Type

Business

Requirements
Must have
• See details above and logo attached
Should not have
• Images other than logo

```html
<!DOCTYPE html>
<html lang="en">
<head>
<meta charset="utf-8">
<title>Ridgeline Projects Australia – Business Card</title>
<link rel="stylesheet" href="https://fonts.googleapis.com/css2?family=Questrial&display=swap">
<style>
  :root {
    --backdrop: #2b2b2b;
    --card-blue: #1a93c8;
    --card-white: #f6f6f6;
    --ink-blue: #1a86bf;
    --ink-grey: #8a8a8a;
    --mark-grey: #d3d3d3;
    --on-blue: #ffffff;
  }
  * { box-sizing: border-box; margin: 0; padding: 0; }
  html, body {
    width: 1200px;
    height: 900px;
    overflow: hidden;
    background: var(--backdrop);
    font-family: "Questrial", "Century Gothic", sans-serif;
  }
  .canvas {
    position: relative;
    width: 1200px;
    height: 900px;
  }
  .card {
    position: absolute;
    width: 560px;
    height: 320px;
    box-shadow: 0 14px 30px rgba(0,0,0,0.55);
  }

  /* Back of card */
  .card--back {
    left: 70px;
    top: 110px;
    background: var(--card-blue);
    color: var(--on-blue);
  }
  .brand {
    position: absolute;
    left: 70px;
    top: 118px;
    display: flex;
    align-items: center;
    gap: 16px;
  }
  .brand__square {
    width: 62px;
    height: 62px;
    background: var(--on-blue);
  }
  .brand__name {
    font-size: 34px;
    line-height: 1;
    letter-spacing: 1px;
    text-transform: uppercase;
  }
  .brand__sub {
    display: block;
    font-size: 14px;
    letter-spacing: 5px;
    margin-top: 6px;
  }
  .tagline {
    position: absolute;
    left: 70px;
    top: 200px;
    font-size: 14px;
    letter-spacing: 0.3px;
  }

  /* Front of card */
  .card--front {
    left: 570px;
    top: 470px;
    background: var(--card-white);
  }
  .holder {
    position: absolute;
    left: 44px;
    top: 96px;
    color: var(--ink-blue);
  }
  .holder__name {
    font-size: 21px;
    letter-spacing: 0.5px;
    text-transform: uppercase;
    font-weight: 400;
  }
  .holder__role {
    font-size: 14px;
    margin-top: 2px;
  }
  .contacts {
    position: absolute;
    left: 44px;
    top: 188px;
    list-style: none;
    font-size: 14px;
    line-height: 19px;
    color: var(--ink-blue);
  }
  .contacts__label {
    display: inline-block;
    width: 20px;
    color: var(--ink-grey);
  }
  .mark {
    position: absolute;
    right: 48px;
    top: 78px;
    width: 160px;
    height: 160px;
    background: var(--mark-grey);
  }
</style>
</head>
<body>
  <main class="canvas">
    <section class="card card--back">
      <div class="brand">
        <span class="brand__square"></span>
        <p class="brand__name">Ridgeline<span class="brand__sub">Projects Australia</span></p>
      </div>
      <p class="tagline">Leaders in Construction Project Management Services</p>
    </section>

    <section class="card card--front">
      <div class="holder">
        <h1 class="holder__name">Tobias Surname</h1>
        <p class="holder__role">Director</p>
      </div>
      <ul class="contacts">
        <li><span class="contacts__label">P:</span>000 123 4567</li>
        <li><span class="contacts__label">E:</span>ridgeline@domain.com</li>
        <li><span class="contacts__label">A:</span>Your Address</li>
        <li><span class="contacts__label">W:</span>ridgeline@com</li>
      </ul>
      <span class="mark"></span>
    </section>
  </main>
</body>
</html>
```